Norvell Property Services LLC. Commercial & Residential

PROFESSIONAL WINDOW WASHING! professional dryer vent cleaning (prevent fires, $aves money, Lowers your electric bill, save your dryer, less drying time, ask how!)gutter clean outs and tune-up *Lowest Price Quotes Guaranteed!Straightforward Consultancy and Advice to empower homeowners and find solutions that fit your budget!non pressure house cleaning "no pressure...No Damage!Interior & Exterior House Painting call for free in-home consultationPre & Post Tenant Clean-Up PaintGenerator Maintenance Comprehensive Landlord Services & REO (special requests considered) no job too small)!

I would like my business cards to be as professional as possible. I provide property services to commercial and residential clients and need these cards to draw attention and catch ones eye. I have never had business cards for this the services I provide. And I need them so that business owners will trust that our services are the best and also homeowners will call based on the information they see on these cards., I want the window washing service to be the main focal point because it the main service provided. thank you Added Saturday, July 4, 2015

Target Market(s)

Property Services and professional window cleaning highlighted on the front of card rounded edges for card and sleek eye catching cards thank you

Industry/Entity Type

Property Maintenance

Contact Information for Business Card

518-555-0147 Direct. norvellpropertyservicesllc@brindlemail.net

Requirements
Must have
• Professional appearance and eye catch design Property Services as a general point with professional window washing as a highlighted service and all the rest of the services on back of card
Nice to have
• vivid colors but professional appearance

```html
<!DOCTYPE html>
<html lang="en">
<head>
<meta charset="utf-8">
<title>Norvell Property Services LLC — Business Card</title>
<link rel="stylesheet" href="https://fonts.googleapis.com/css2?family=Arimo:wght@400;700&display=swap">
<style>
  :root {
    --backdrop: #d6d6d4;
    --card-white: #ffffff;
    --panel-steel-top: #3a3a3a;
    --panel-steel-bottom: #1c1c1c;
    --panel-black: #050505;
    --panel-red-top: #8e1a1a;
    --panel-red-bottom: #5e0d0f;
    --mark-grey: #6b6b6b;
    --text-white: #ffffff;
    --text-soft: #d4d4d4;
    --text-accent: #e03a3a;
    --icon-ring: #ffffff;
    --icon-fill: #8a8a8a;
  }
  html, body {
    margin: 0;
    padding: 0;
    width: 1200px;
    height: 873px;
    overflow: hidden;
    background: var(--backdrop);
  }
  .business-card {
    position: absolute;
    left: 110px;
    top: 148px;
    width: 980px;
    height: 578px;
    box-shadow: 0 10px 30px rgba(0, 0, 0, 0.25);
  }
  .business-card svg { display: block; }
  .card-text { font-family: "Arimo", Arial, sans-serif; }
  .service-title { fill: var(--text-white); font-size: 35px; letter-spacing: 0.5px; }
  .service-highlight { fill: var(--text-accent); font-size: 24px; font-weight: 700; letter-spacing: 0.5px; }
  .service-tagline { fill: var(--text-soft); font-size: 23px; }
  .company-name { fill: var(--text-white); font-size: 23px; }
  .contact-line { fill: var(--text-soft); font-size: 27px; }
</style>
</head>
<body>
<div class="business-card">
  <svg width="980" height="578" viewBox="0 0 980 578" xmlns="http://www.w3.org/2000/svg">
    <defs>
      <linearGradient id="steel-gradient" x1="0" y1="0" x2="0" y2="1">
        <stop offset="0" stop-color="var(--panel-steel-top)"/>
        <stop offset="1" stop-color="var(--panel-steel-bottom)"/>
      </linearGradient>
      <linearGradient id="red-gradient" x1="0" y1="0" x2="1" y2="1">
        <stop offset="0" stop-color="var(--panel-red-top)"/>
        <stop offset="1" stop-color="var(--panel-red-bottom)"/>
      </linearGradient>
    </defs>

    <rect class="card-base" width="980" height="578" fill="var(--card-white)"/>

    <!-- brushed steel panel -->
    <polygon class="steel-panel" role="img" aria-label="Dark brushed metal texture panel"
             points="0,0 302,0 414,258 372,578 0,578" fill="url(#steel-gradient)"/>

    <!-- headline panel -->
    <polygon class="headline-panel" points="322,0 980,0 980,235 426,235" fill="var(--panel-black)"/>

    <!-- contact panel -->
    <polygon class="contact-panel" points="436,284 980,284 980,578 390,578" fill="url(#red-gradient)"/>

    <!-- company mark placeholder and name -->
    <circle class="company-mark" cx="160" cy="235" r="62" fill="var(--mark-grey)"/>
    <text class="card-text company-name" x="25" y="424">Norvell Property Services LLC</text>

    <!-- headline -->
    <text class="card-text service-title" x="453" y="70">PROPERTY MAINTENANCE</text>
    <text class="card-text service-highlight" x="453" y="118">PROFESSIONAL WINDOW WASHING</text>
    <text class="card-text service-tagline" x="453" y="163">no job too small, fit in your budget</text>

    <!-- phone -->
    <g class="contact-icon phone-icon">
      <circle cx="498" cy="372" r="30" fill="var(--icon-fill)" stroke="var(--icon-ring)" stroke-width="7"/>
      <rect x="487" y="359" width="22" height="26" rx="4" fill="var(--icon-ring)"/>
      <rect x="491" y="364" width="14" height="13" fill="var(--icon-fill)"/>
    </g>
    <text class="card-text contact-line" x="541" y="382">518-555-0147</text>

    <!-- email -->
    <g class="contact-icon mail-icon">
      <circle cx="498" cy="466" r="30" fill="var(--icon-fill)" stroke="var(--icon-ring)" stroke-width="7"/>
      <rect x="484" y="456" width="28" height="20" rx="2" fill="var(--icon-ring)"/>
      <polyline points="484,457 498,468 512,457" fill="none" stroke="var(--icon-fill)" stroke-width="2.5"/>
    </g>
    <text class="card-text contact-line" x="541" y="452">norvellpropertyservicesllc@</text>
    <text class="card-text contact-line" x="541" y="489">brindlemail.net</text>
  </svg>
</div>
</body>
</html>
```